Simple and Clean business card design

We would like the design to be simple clean and to incorporate our colors.

We are open to your design and talent, we have the dots in our logo as we think of it as data points and we connect data points for people.

We are open to see the great creative and clean design you bring to the table

Contact Information for Business Card

please include: name, position, email, phone and website

Font styles to use
Sans Serif

Requirements
Must have
• my colors incorporated, simplicity
Nice to have
• lots of white space, simplicity
Should not have
• complexicity/ complex art

```html
<!DOCTYPE html>
<html lang="en">
<head>
<meta charset="utf-8">
<title>Dotwise Business Card</title>
<link rel="stylesheet" href="https://fonts.googleapis.com/css2?family=Arimo:wght@400;700&display=swap">
<style>
  :root {
    --bg: #2a2a2a;
    --card-white: #f6f6f6;
    --ink: #111111;
    --blue: #4a86e8;
    --teal: #48a7a0;
    --green: #3cb464;
    --yellow: #f8cd0c;
    --orange: #f39325;
    --red: #e94a35;
    --divider: #333333;
  }
  * { box-sizing: border-box; margin: 0; padding: 0; }
  html, body { width: 1200px; height: 901px; overflow: hidden; }
  body {
    background: var(--bg);
    font-family: "Arimo", Arial, sans-serif;
    display: flex;
    flex-direction: column;
    align-items: center;
    justify-content: center;
    gap: 56px;
  }
  .card {
    width: 600px;
    height: 343px;
    position: relative;
    box-shadow: 0 12px 30px rgba(0,0,0,0.5);
  }
  .card-front {
    background: linear-gradient(90deg, var(--blue) 0%, var(--teal) 25%, var(--green) 45%, var(--yellow) 72%, var(--orange) 85%, var(--red) 100%);
    display: flex;
    align-items: center;
    justify-content: center;
  }
  .wordmark {
    display: flex;
    align-items: center;
    gap: 14px;
    font-weight: 700;
    font-size: 66px;
    letter-spacing: 1px;
    color: var(--ink);
  }
  .wordmark-dot {
    width: 22px; height: 22px; border-radius: 50%;
  }
  .card-front .wordmark-dot { background: #ffffff; }
  .card-back .wordmark-dot { background: var(--green); }
  .card-back {
    background: var(--card-white);
    padding-top: 44px;
  }
  .card-back .wordmark { justify-content: center; font-size: 64px; }
  .details {
    display: flex;
    justify-content: center;
    margin-top: 34px;
  }
  .identity {
    text-align: right;
    padding-right: 22px;
    border-right: 1.5px solid var(--divider);
    padding-top: 6px;
  }
  .person-name {
    color: var(--blue);
    font-weight: 700;
    font-size: 25px;
  }
  .person-title {
    font-size: 16px;
    color: var(--ink);
    margin-top: 2px;
  }
  .contacts {
    list-style: none;
    padding-left: 20px;
    font-size: 16px;
    color: var(--ink);
    display: flex;
    flex-direction: column;
    gap: 9px;
  }
  .contacts li { display: flex; align-items: center; gap: 12px; }
  .contacts svg { width: 16px; height: 16px; flex: none; }
  .address {
    text-align: center;
    font-size: 16px;
    color: var(--ink);
    margin-top: 30px;
  }
</style>
</head>
<body>
  <section class="card card-front">
    <div class="wordmark"><span>Dotwise</span><span class="wordmark-dot"></span></div>
  </section>

  <section class="card card-back">
    <div class="wordmark"><span>Dotwise</span><span class="wordmark-dot"></span></div>
    <div class="details">
      <div class="identity">
        <p class="person-name">Daniel Harper</p>
        <p class="person-title">Manager</p>
      </div>
      <ul class="contacts">
        <li>
          <svg viewBox="0 0 16 16" aria-hidden="true"><path d="M4 1.5 L6.2 4.5 L5 6 Q6.5 9.5 10 11 L11.5 9.8 L14.5 12 L13 14.5 Q6 14 1.5 3 Z" fill="var(--blue)"/></svg>
          <span>555-018-2746</span>
        </li>
        <li>
          <svg viewBox="0 0 16 16" aria-hidden="true"><rect x="1.5" y="3.5" width="13" height="9" rx="1" fill="none" stroke="var(--green)" stroke-width="1.4"/><path d="M1.5 4 L8 9 L14.5 4" fill="none" stroke="var(--green)" stroke-width="1.4"/></svg>
          <span>youremail@example.com</span>
        </li>
        <li>
          <svg viewBox="0 0 16 16" aria-hidden="true"><g fill="none" stroke="var(--yellow)" stroke-width="1.3"><circle cx="8" cy="8" r="6.5"/><ellipse cx="8" cy="8" rx="3" ry="6.5"/><path d="M1.5 8 H14.5 M2.5 4.8 H13.5 M2.5 11.2 H13.5"/></g></svg>
          <span>www.yourwebsite.com</span>
        </li>
      </ul>
    </div>
    <p class="address">Your address, city, state, ZIP 0000</p>
  </section>
</body>
</html>
```